Now Open Poster

We need a banner for our sports supplement and nutritional store, Harbor Nutrition.
We were hoping for some sort of creative word art piece.
I have drawn my own mock up just to give you all a very basic starting point. But you are free to go with whatever you feel will work best.
The primary objective is simply to explain a little about what the company does, and then direct traffic towards the store with an 'Open Arrow' pointing left.
Text words we have chosen are:
Protein
Creatine
Health
Fitness
Sports Science
Nutrition
Energy
Achievement
Amino Acids
Organic
Supplements
Performance
Testosterone Support
Vitamins
Growth
Diet
Happiness
Weight Loss
Strong
Natural
Vitality
Accomplished
Below the word art we want our logo (See attached options)
Then below the logo the phrase "Success Starts Here"
Dimensions of the poster are 140cm x 60cm.
Colours: Blues/Whites/Greys/Blacks (Lots of white space please)
Here are some cool pieces I found that had some interesting elements that I liked (I'd love to see a mash-up of styles with a street art feel to it. Something funky!):
http://www.moodgrove.example/pin/804417263190552871/
http://www.moodgrove.example/pin/615380924471208539/
http://www.moodgrove.example/pin/804417263192736155/
http://www.moodgrove.example/pin/804417263194418620/
http://www.moodgrove.example/pin/937162048856301742/
Thanks for reading, message me if you have any further questions!
- Tobias

```html
<!DOCTYPE html>
<html lang="en">
<head>
<meta charset="utf-8">
<title>Harbor Nutrition — Now Open</title>
<link rel="stylesheet" href="https://fonts.googleapis.com/css2?family=Alfa+Slab+One&family=Cabin+Sketch:wght@700&family=Cinzel:wght@700&family=Fascinate&family=Gochi+Hand&family=Josefin+Sans:wght@300;700&family=Lobster&family=Montserrat:wght@800&family=Noto+Serif&family=Oswald:wght@300;400;700&family=Playball&family=Playfair+Display:ital,wght@1,700&family=Questrial&family=Rye&family=Sniglet&display=swap">
<style>
  :root {
    --page: #ffffff;
    --paper-light: #ffffff;
    --paper-dark: #e9eef3;
    --paper-edge: #b9c7d4;
    --navy: #22384f;
    --steel: #3f6e96;
    --sky: #7fa6c9;
    --grey: #8a939c;
    --snow: #f7f9fb;
  }
  * { margin: 0; padding: 0; box-sizing: border-box; }
  html, body { width: 1200px; height: 900px; overflow: hidden; background: var(--page); }
  .canvas { position: relative; width: 1200px; height: 900px; }

  .poster {
    position: absolute; left: 411px; top: 38px;
    width: 368px; height: 864px;
    background: radial-gradient(ellipse at 50% 45%, var(--paper-light) 45%, var(--paper-dark) 100%);
    box-shadow: inset 0 0 0 1px var(--paper-edge), inset 0 0 6px var(--paper-edge);
  }
  .word { position: absolute; white-space: nowrap; line-height: 1; }

  .open { left: 107px; top: 40px; font: 700 48px "Cabin Sketch", sans-serif; color: var(--navy); }
  .rule { position: absolute; left: 32px; width: 302px; height: 0; border-top: 1px solid var(--steel); }
  .plaque { position: absolute; left: 142px; top: 90px; width: 80px; height: 90px; border-radius: 30px; background: var(--navy); box-shadow: 0 0 0 3px var(--sky); }
  .protein { left: 30px; top: 127px; font: 37px "Playball", cursive; color: var(--sky); }
  .fitness { left: 226px; top: 135px; font: 300 27px "Josefin Sans", sans-serif; color: var(--navy); }
  .weight-loss { left: 36px; top: 172px; font: 700 21px/21px "Josefin Sans", sans-serif; color: var(--grey); text-align: center; letter-spacing: 1px; }
  .health { left: 142px; top: 180px; font: 40px "Lobster", cursive; color: var(--steel); letter-spacing: 1px; }
  .spiral { position: absolute; left: 271px; top: 180px; width: 50px; height: 44px; border-radius: 50%; background: var(--steel); opacity: .75; }
  .nutrition { left: 35px; top: 216px; font: 43px "Noto Serif", serif; color: var(--navy); }
  .closer { left: 231px; top: 234px; font: 36px "Gochi Hand", cursive; color: var(--sky); letter-spacing: 2px; }
  .heart { position: absolute; left: 313px; top: 224px; width: 16px; height: 14px; border-radius: 50%; background: var(--sky); }
  .gain { left: 35px; top: 272px; font: 49px "Fascinate", cursive; color: var(--steel); }
  .creatine { left: 164px; top: 265px; font: 700 62px "Oswald", sans-serif; color: var(--navy); letter-spacing: -1px; transform: scaleX(.86); transform-origin: left; }
  .strength { left: 33px; top: 328px; font: italic 700 41px "Playfair Display", serif; color: var(--navy); }
  .brace { left: 202px; top: 330px; font: 300 66px "Oswald", sans-serif; color: var(--sky); }
  .better { left: 220px; top: 334px; font: 400 28px "Oswald", sans-serif; color: var(--steel); transform: scaleX(.92); transform-origin: left; }
  .than { left: 223px; top: 369px; font: 400 28px "Oswald", sans-serif; color: var(--steel); }
  .divider { position: absolute; left: 279px; top: 372px; width: 0; height: 200px; border-left: 1px solid var(--navy); }
  .yesterday { left: 292px; top: 366px; font: 300 38px "Oswald", sans-serif; color: var(--steel); writing-mode: vertical-rl; letter-spacing: 6px; }
  .growth { left: 33px; top: 378px; font: 700 32px "Cinzel", serif; color: var(--grey); }
  .vitamins { left: 35px; top: 410px; font: 48px "Questrial", sans-serif; color: var(--navy); letter-spacing: 2px; }
  .herbs { left: 36px; top: 453px; font: 800 32px "Montserrat", sans-serif; color: var(--steel); letter-spacing: -.5px; }
  .organic { left: 44px; top: 488px; font: 44px "Sniglet", sans-serif; color: var(--navy); letter-spacing: 3px; }
  .leaf { position: absolute; left: 238px; top: 486px; width: 18px; height: 22px; border-radius: 50% 50% 50% 0; background: var(--steel); }
  .energy { left: 39px; top: 534px; font: 42px "Rye", serif; color: var(--sky); }
  .diet { left: 240px; top: 518px; font: 23px "Alfa Slab One", serif; color: var(--navy); writing-mode: vertical-rl; }

  .tagline-band {
    position: absolute; left: 44px; top: 589px; width: 293px; height: 40px;
    background: var(--navy); border-left: 3px double var(--snow); border-right: 3px double var(--snow);
    display: flex; align-items: center; justify-content: center;
    font: 30px "Alfa Slab One", serif; color: var(--snow); letter-spacing: 1px;
  }

  .brand { position: absolute; left: 32px; top: 642px; width: 302px; height: 126px; display: flex; align-items: center; gap: 18px; }
  .brand-dot { width: 124px; height: 124px; border-radius: 50%; border: 5px solid var(--navy); flex: none; }
  .brand-name { font: 28px/32px "Alfa Slab One", serif; color: var(--navy); }

  .success { left: 41px; top: 787px; font: 700 29px "Cabin Sketch", sans-serif; color: var(--grey); }
</style>
</head>
<body>
<div class="canvas">
  <section class="poster" aria-label="Harbor Nutrition now open poster">
    <h1 class="word open">OPEN</h1>
    <div class="rule" style="top:119px"></div>
    <div class="rule" style="top:124px"></div>
    <div class="plaque" role="img" aria-label="Keyhole plaque ornament"></div>

    <span class="word protein">Protein</span>
    <span class="word fitness">FITNESS</span>
    <span class="word weight-loss">WEIGHT<br>LOSS</span>
    <span class="word health">Health</span>
    <div class="spiral" role="img" aria-label="Spiral ornament"></div>
    <span class="word nutrition">Nutrition</span>
    <span class="word closer">closer</span>
    <div class="heart" role="img" aria-label="Small heart ornament"></div>
    <span class="word gain">Gain</span>
    <span class="word creatine">Creatine</span>
    <span class="word strength">Strength</span>
    <span class="word brace">{</span>
    <span class="word better">I am better</span>
    <span class="word than">than</span>
    <div class="divider"></div>
    <span class="word yesterday">YESTERDAY</span>
    <span class="word growth">GROWTH</span>
    <span class="word vitamins">VITAMINS</span>
    <span class="word herbs">Natural Herbs</span>
    <span class="word organic">organic</span>
    <div class="leaf" role="img" aria-label="Small leaf ornament"></div>
    <span class="word energy">ENERGY</span>
    <span class="word diet">DIET</span>

    <p class="tagline-band">I AM HARBOR.</p>

    <div class="brand">
      <span class="brand-dot"></span>
      <span class="brand-name">Harbor<br>Nutrition</span>
    </div>

    <p class="word success">SUCCESS STARTS HERE.</p>
  </section>
</div>
</body>
</html>
```